Website Page Re-Design

I have 2 pages that need to be re-designed on my site. This is the site so you can take a look and get a feel for the layout etc, www.vortaplay.com
I have included screen shots of the individual pages I want redone as well as some examples from other sites for ideas.

Homepage Story, would like the redo sunday file, to be made stunning, only the content, picture and share buttons need be altered the, would like and emphasis on intergrating the share buttons, the story page starts here http://www.vortaplay.com/league/ball-hockey/mens/news-division/ so what is beingcreated is when the read more is clicked

Free Agent Forms:
Needs to be re-worked so that there isn't so much white space on the page.

Industry/Entity Type

News

Requirements
Must have
• share buttons to slick very well intergrated
Nice to have
• Share buttons to be top notch

```html
<!DOCTYPE html>
<html lang="en">
<head>
<meta charset="utf-8">
<title>Vortaplay – League News</title>
<link href="https://fonts.googleapis.com/css2?family=Montserrat:wght@700;800&family=Ubuntu:ital,wght@0,400;0,500;0,700;1,500&display=swap" rel="stylesheet">
<style>
:root{
  --bg:#86bb45;
  --bg-light:#a9d26d;
  --panel:#e6f1d5;
  --panel-edge:#f4f9ec;
  --ink:#111;
  --pale-nav:#f5f6bf;
  --green-text:#7db23c;
  --green-dark:#5f9a26;
  --frame:#8bbd4c;
  --white:#fff;
}
*{box-sizing:border-box;margin:0;padding:0}
html,body{width:1200px;height:682px;overflow:hidden}
body{
  position:relative;
  font-family:"Ubuntu",sans-serif;
  background:radial-gradient(ellipse at 50% 20%,var(--bg-light) 0%,var(--bg) 55%,#79b03a 100%);
}
.logo{position:absolute;left:204px;top:18px;display:flex;align-items:center;gap:8px;color:var(--white);font-weight:700;font-size:34px;letter-spacing:-1px}
.logo-mark{width:14px;height:14px;background:var(--white);border-radius:50%}
.top-nav{position:absolute;left:649px;top:0;width:351px;height:22px;background:var(--pale-nav);border-radius:0 0 6px 6px;display:flex;align-items:center;padding:0 4px}
.top-nav a{color:var(--ink);text-decoration:none;font-size:12px;flex:1;text-align:center;border-right:1px solid #b2a355;line-height:18px}
.top-nav a:last-child{border-right:none}
.main-nav{position:absolute;left:525px;top:34px;width:475px;height:42px;background:#141414;border-radius:6px 2px 8px 3px;display:flex;align-items:center;justify-content:flex-end;padding-right:22px}
.main-nav a{color:var(--white);font-style:italic;font-weight:500;font-size:12.5px;text-decoration:underline;padding:0 9px;border-left:1px solid #666;line-height:13px}
.main-nav a:first-child{border-left:none}
.panel{position:absolute;left:201px;top:88px;width:800px;height:518px;background:var(--panel);border-radius:8px;border:2px solid var(--panel-edge)}
.banner{position:absolute;left:13px;top:9px;width:775px;height:92px;background:linear-gradient(180deg,#8fc14e,#5d962a);border-radius:3px;overflow:hidden}
.banner-photo{position:absolute;left:15px;top:-12px;width:540px;height:104px;background:linear-gradient(90deg,#c27b5a,#b7373a 40%,#d97a40 65%,#d2d2c8);opacity:.85}
.follow{position:absolute;left:594px;top:19px;width:140px;height:54px;background:#0d0d0d;border-radius:6px;display:flex;align-items:center;gap:10px;padding-left:13px;color:var(--white);font-style:italic;font-weight:500;font-size:13px;line-height:13px}
.follow-mark{width:28px;height:28px;background:#3e5f9c;border-radius:4px}
.article-head{position:absolute;left:13px;top:116px;width:522px;height:37px;background:linear-gradient(180deg,#444,#050505);border-radius:4px 4px 0 0;color:var(--white);display:flex;align-items:center;justify-content:center;gap:10px;font-family:"Montserrat",sans-serif;font-weight:800;font-size:14.5px}
.article-head svg{width:20px;height:10px}
.photo-frame{position:absolute;left:13px;top:153px;width:522px;height:350px;background:var(--frame)}
.article-photo{position:absolute;left:12px;top:7px;width:498px;height:331px;background:linear-gradient(180deg,#2f59b8 0%,#3567c4 45%,#e5e5e5 60%,#2e8a4e 85%,#257a40 100%)}
.share-bar{position:absolute;left:554px;top:116px;display:flex;gap:4px}
.share{width:44px;display:flex;flex-direction:column;align-items:center;gap:6px}
.share .count{width:44px;height:24px;background:var(--white);border:1px solid #cfe0ea;border-radius:2px;font-size:9px;display:flex;align-items:center;justify-content:center;color:#222}
.share .btn{width:44px;height:16px;border-radius:2px;color:var(--white);font-size:8.5px;display:flex;align-items:center;justify-content:center}
.btn.share-fb{background:#4b67a4}.btn.share-tw{background:#38a7dc}.btn.share-plus{background:#f2f2f2;color:#d03b2c;border:1px solid #ccc}.btn.share-mail{background:#5b8fc8}.btn.share-comment{background:#4f9a1e;font-weight:700}
.post-date{position:absolute;left:555px;top:180px;width:33px;height:40px;border:3px solid var(--green-dark);border-radius:3px;background:var(--panel);text-align:center;color:var(--green-dark)}
.post-date .m{display:block;background:var(--green-dark);color:var(--white);font-size:5px;line-height:8px}
.post-date .d{font-size:15px;font-weight:700;line-height:24px}
.post-title{position:absolute;left:599px;top:184px;font-family:"Montserrat",sans-serif;font-weight:800;font-size:16.5px;line-height:17px;color:var(--green-dark)}
.dots{position:absolute;left:555px;top:227px;width:192px;border-top:2px dotted #a6cc7c}
.post-body{position:absolute;left:555px;top:239px;width:208px;font-size:10.4px;line-height:13.55px;color:var(--green-text)}
.read-more{position:absolute;left:555px;top:494px;font-size:10px;font-weight:700;color:var(--green-dark);text-decoration:none}
.footer{position:absolute;left:201px;top:635px;font-size:8.5px;letter-spacing:.5px;color:var(--white)}
</style>
</head>
<body>
<div class="logo"><span class="logo-mark"></span>Vortaplay</div>

<nav class="top-nav">
  <a href="#">Home</a><a href="#">About Us</a><a href="#">FAQS</a><a href="#">Contact Us</a><a href="#">Jobs</a>
</nav>

<nav class="main-nav">
  <a href="#">Leagues</a><a href="#">Schedules &amp; More</a><a href="#">Register</a><a href="#">Pay</a><a href="#">Forum</a><a href="#">Sponsors</a>
</nav>

<main class="panel">
  <div class="banner">
    <div class="banner-photo" role="img" aria-label="Row of league players in jerseys and caps"></div>
    <div class="follow"><span class="follow-mark"></span><span>Find Us On<br>Chatterly</span></div>
  </div>

  <header class="article-head">
    <svg viewBox="0 0 20 10"><path d="M1 1l4 4-4 4M7 1l4 4-4 4M13 1l4 4-4 4" fill="none" stroke="#fff" stroke-width="1.6"/></svg>
    Lorem Ipsum Dolor Sit Amet Consectetuer
    <svg viewBox="0 0 20 10"><path d="M1 1l4 4-4 4M7 1l4 4-4 4M13 1l4 4-4 4" fill="none" stroke="#fff" stroke-width="1.6"/></svg>
  </header>
  <div class="photo-frame">
    <div class="article-photo" role="img" aria-label="Team group photo in white shirts holding a large charity cheque on an indoor rink"></div>
  </div>

  <div class="share-bar">
    <div class="share"><span class="count">11</span><span class="btn share-fb">share</span></div>
    <div class="share"><span class="count" style="color:#2a8ac4">10</span><span class="btn share-tw">tweet</span></div>
    <div class="share"><span class="count" style="font-size:12px">2</span><span class="btn share-plus">+1</span></div>
    <div class="share"><span class="count">3</span><span class="btn share-mail">email</span></div>
    <div class="share"><span class="count">6</span><span class="btn share-comment">comment</span></div>
  </div>

  <div class="post-date"><span class="m">June</span><span class="d">28</span></div>
  <h2 class="post-title">LOREM IPSUM<br>DOLOR SIT AMET</h2>
  <div class="dots"></div>
  <p class="post-body">Aliquam Erat Volutpat. Ut Wisi Enim Ad Minim Veniam, Quis Nostrud Exerci Tation Ullamcorper Suscipit Lobortis Nisl Ut Aliquip Ex Ea Commodo Consequat. Duis Autem Vel Eum Iriure Dolor In Hendrerit In Vulputate Velit Esse Molestie Consequat, Vel Illum Dolore Eu Feugiat Nulla Facilisis At Vero Eros Et Accumsan Et Iusto Odio Dignissim Qui Blandit Praesent Luptatum Zzril Delenit Augue Duis Dolore Te Feugait Nulla Facilisi.volutpat. Ut Wisi Enim Ad Minim Veniam, Quis Nostrud Exerci Tation Ullamcorper Suscipit Lobortis Nisl Ut Aliquip Ex Ea Commodo Consequat. Duis Autem Vel Eum Iriure Dolor In Hendrerit In Vulputate Velit Esse Molestie Consequat.Ex Ea Commodo Consequat. Duis Autem Vel Eum Iriure Dolor.</p>
  <a class="read-more" href="#">READMORE &gt;&gt;</a>
</main>

<footer class="footer">© 2011, VORTAPLAY. ALL RIGHTS RESERVED.</footer>
</body>
</html>
```